Re-design of current business cards

We are updating our website with new colors and layout. Would like to re-design our business cards to co-ordinate. See attached pdf with new Brightwell website colors. We would also like to combine our 2 brands on the one business card. Attached is the new design for our Brightwell website, current business cards, which are one sided, brightwell logo in tiff, .ai for fonts. Brightwell logo font is Optimum, Lanterncove website home page image, Lanterncove brand statics for products which includes the logo for this brand.

Lanterncove brand will stay the dark gray on the website. See attached statics for product and website home page.
Updates

The business cards will be 2 sided. Brightwell Brand on one side and Lanterncove Brand on the other. The colors for Brightwell need to follow the color scheme of the brightwell website pdf I uploaded. The colors are a blue, lighter teal blue and white. Lanterncove needs to follow the dark gray color on files uploaded

Target Market(s)

The trade and consumers

Industry/Entity Type

Home Furnishing

Contact Information for Business Card

We are updating our website with new colors and layout. Would like to re-design our business cards to co-ordinate. We would also like to combine our 2 brands onto 1 2 sided business cards.

Requirements
Must have
• Colors that match our new website, see attached image.
• RGB colors
• navy -#152842
• teal - 98aeb9
• The gray color used for Lanterncove brands.
• ll logos and fonts should stay the same.

```html
<!DOCTYPE html>
<html lang="en">
<head>
<meta charset="utf-8">
<title>Brightwell &amp; Lanterncove Business Cards</title>
<link href="https://fonts.googleapis.com/css2?family=Open+Sans:wght@300;400;600;700&display=swap" rel="stylesheet">
<style>
  :root {
    --page-bg: #ecebe8;
    --card-white: #ffffff;
    --brand-navy: #152842;
    --brand-teal: #98aeb9;
    --ink-text: #152842;
    --icon-ink: #3b4a5e;
    --lanterncove-gray: #5b5d5f;
    --on-dark: #f4f4f4;
  }
  * { margin: 0; padding: 0; box-sizing: border-box; }
  html, body {
    width: 1200px; height: 900px; overflow: hidden;
    background: var(--page-bg);
    font-family: "Open Sans", Arial, sans-serif;
  }
  .canvas {
    position: relative; width: 1200px; height: 900px;
    display: flex; align-items: center; justify-content: center; gap: 40px;
  }
  .card {
    position: relative; width: 520px; height: 297px; overflow: hidden;
    box-shadow: 0 6px 18px rgba(0,0,0,0.18);
  }

  /* Lanterncove side */
  .card--lanterncove { background: var(--lanterncove-gray); color: var(--on-dark); }
  .lanterncove-mark {
    position: absolute; left: 0; right: 0; top: 92px; text-align: center;
  }
  .lanterncove-name {
    display: block;
    font-size: 40px; font-weight: 300; letter-spacing: 1px; line-height: 1.1;
    color: var(--on-dark); text-transform: uppercase;
  }
  .lanterncove-by {
    display: block; font-size: 8px; font-weight: 300; letter-spacing: 1px;
    text-transform: uppercase; text-align: right; padding-right: 104px;
    margin-top: 1px; color: var(--on-dark);
  }
  .lanterncove-tagline {
    position: absolute; left: 0; right: 0; top: 186px; text-align: center;
    font-size: 15px; font-weight: 300; color: var(--on-dark);
  }

  /* Brightwell side */
  .card--brightwell { background: var(--card-white); color: var(--ink-text); }
  .card-curves { position: absolute; inset: 0; }
  .holder { position: absolute; left: 30px; top: 30px; }
  .holder-name {
    font-size: 20px; font-weight: 700; color: var(--brand-teal);
    text-transform: uppercase; letter-spacing: 0.5px; line-height: 1.15;
  }
  .holder-title { font-size: 13.5px; color: var(--ink-text); margin-top: 1px; }

  .brightwell-mark {
    position: absolute; right: 24px; top: 28px;
    display: flex; flex-direction: column; align-items: flex-end;
  }
  .brightwell-dot {
    width: 36px; height: 36px; border-radius: 50%; background: var(--brand-teal);
    margin-right: 130px;
  }
  .brightwell-name {
    font-size: 33px; font-weight: 400; color: var(--brand-navy);
    text-transform: uppercase; letter-spacing: 1px; line-height: 1.2; margin-top: 2px;
  }

  .contact-list {
    position: absolute; left: 30px; top: 134px; list-style: none;
  }
  .contact-list li {
    display: flex; align-items: center; gap: 8px;
    font-size: 15px; line-height: 20px; color: var(--ink-text);
  }
  .contact-icon { width: 12px; height: 12px; fill: var(--icon-ink); flex: none; }

  .address {
    position: absolute; right: 22px; top: 222px; text-align: right;
    font-style: normal; font-size: 12.5px; line-height: 18px; color: var(--on-dark);
  }
</style>
</head>
<body>
<main class="canvas">

  <section class="card card--lanterncove" aria-label="Lanterncove side">
    <div class="lanterncove-mark">
      <span class="lanterncove-name">Lanterncove</span>
      <span class="lanterncove-by">by Brightwell</span>
    </div>
    <p class="lanterncove-tagline">Discover the luxury of home.</p>
  </section>

  <section class="card card--brightwell" aria-label="Brightwell side">
    <svg class="card-curves" viewBox="0 0 520 297" width="520" height="297" aria-hidden="true">
      <path d="M0 230 C140 262 290 238 420 160 C310 230 160 256 0 250 Z" fill="var(--brand-teal)"/>
      <path d="M0 266 C170 268 335 218 520 142 L520 297 L0 297 Z" fill="var(--brand-navy)"/>
    </svg>

    <div class="holder">
      <h1 class="holder-name">Dana Whitfield</h1>
      <p class="holder-title">Graphics/Photography Director</p>
    </div>

    <div class="brightwell-mark">
      <span class="brightwell-dot"></span>
      <span class="brightwell-name">Brightwell</span>
    </div>

    <ul class="contact-list">
      <li>
        <svg class="contact-icon" viewBox="0 0 12 12" aria-hidden="true"><path d="M1 4 C1 2 3 1 6 1 C9 1 11 2 11 4 L8.5 4.6 L8 3.4 C7 3 5 3 4 3.4 L3.5 4.6 Z M3 6 L9 6 L10 11 L2 11 Z"/></svg>
        555.201.4830
      </li>
      <li>
        <svg class="contact-icon" viewBox="0 0 12 12" aria-hidden="true"><path d="M3 1 H9 V4 H3 Z M1 5 H11 V9 H9 V7 H3 V9 H1 Z M3.5 8 H8.5 V11 H3.5 Z"/></svg>
        555.201.4877
      </li>
      <li>
        <svg class="contact-icon" viewBox="0 0 12 12" aria-hidden="true"><path d="M1 2.5 H11 V10 H1 Z"/><path d="M1 2.5 L6 7 L11 2.5" fill="none" stroke="#fff" stroke-width="1"/></svg>
        dwhitfield@brightwell.com
      </li>
      <li>
        <svg class="contact-icon" viewBox="0 0 12 12" aria-hidden="true"><circle cx="6" cy="6" r="5"/></svg>
        www.brightwell.com
      </li>
    </ul>

    <address class="address">
      PO Box 214/1180 Maple Ridge Rd<br>
      Alder Falls, Vermont 05731
    </address>
  </section>

</main>
</body>
</html>
```